Lanterns Over the Copper Meadow

This book cover must convey the fact that the scientific evidence is clear that the afterlife is a reality. Attached are two ideas, but they're not working for me as they are. It could be that I'm not a graphic artist and can't get the composition correct. If there is a view of the afterlife, it must be realistic. The afterlife is just like this life. We can't use the family photo. I don't have permission.

```html
<!DOCTYPE html>
<html lang="en">
<head>
<meta charset="utf-8">
<title>Lanterns Over the Copper Meadow</title>
<link rel="stylesheet" href="https://fonts.googleapis.com/css2?family=Anton&display=swap">
<style>
  :root {
    --page: #ffffff;
    --title-blue: #6ea3cf;
    --title-deep: #3f5f9a;
    --title-light: #d4f3fb;
    --glow: rgba(255,255,255,0.95);
    --ring: #2b2f33;
    --lens-edge: #a9d3e6;
  }
  html, body {
    margin: 0;
    width: 1200px;
    height: 1153px;
    overflow: hidden;
    background: var(--page);
  }
  .book-cover {
    position: absolute;
    left: 304px;
    top: 118px;
    width: 609px;
    height: 904px;
    overflow: hidden;
    box-shadow: 0 1px 4px rgba(0,0,0,0.18);
    font-family: "Anton", "Impact", sans-serif;
  }
  .cover-art {
    position: absolute;
    inset: 0;
  }
  .title {
    position: absolute;
    left: 0;
    width: 100%;
    margin: 0;
    text-align: center;
    font-weight: 400;
    line-height: 1;
    color: var(--title-blue);
    text-shadow: 0 0 6px var(--glow), 0 0 2px var(--glow);
  }
  .title-top { top: 103px; font-size: 96px; letter-spacing: 1px; }
  .title-mid { top: 217px; font-size: 44px; }
  .title-main {
    top: 271px;
    font-size: 120px;
    letter-spacing: 2px;
    background: linear-gradient(180deg, var(--title-light) 0%, #9fd4ec 40%, #6b8fc2 72%, var(--title-deep) 100%);
    -webkit-background-clip: text;
    background-clip: text;
    color: transparent;
    text-shadow: none;
    filter: drop-shadow(0 0 3px var(--glow));
  }
  .author {
    position: absolute;
    left: 0;
    width: 100%;
    top: 822px;
    margin: 0;
    text-align: center;
    font-size: 36px;
    line-height: 1;
    color: var(--title-blue);
    text-shadow: 0 0 5px var(--glow);
  }
</style>
</head>
<body>
  <div class="book-cover">
    <svg class="cover-art" width="609" height="904" viewBox="0 0 609 904" xmlns="http://www.w3.org/2000/svg">
      <defs>
        <linearGradient id="meadowBg" x1="0" y1="0" x2="0" y2="1">
          <stop offset="0" stop-color="#f2f3f0"/>
          <stop offset="0.16" stop-color="#c5d4ae"/>
          <stop offset="0.42" stop-color="#7fa35a"/>
          <stop offset="0.68" stop-color="#a9c88a"/>
          <stop offset="0.86" stop-color="#e6efdb"/>
          <stop offset="1" stop-color="#f8faf5"/>
        </linearGradient>
        <radialGradient id="centerMist" cx="0.45" cy="0.55" r="0.45">
          <stop offset="0" stop-color="#ffffff" stop-opacity="0.75"/>
          <stop offset="1" stop-color="#ffffff" stop-opacity="0"/>
        </radialGradient>
        <linearGradient id="lensScene" x1="0" y1="0" x2="0" y2="1">
          <stop offset="0" stop-color="#e4ebea"/>
          <stop offset="0.35" stop-color="#c9c8bf"/>
          <stop offset="0.55" stop-color="#b39a8e"/>
          <stop offset="0.75" stop-color="#8f8a72"/>
          <stop offset="0.9" stop-color="#9ebf7e"/>
          <stop offset="1" stop-color="#d6e8c6"/>
        </linearGradient>
        <radialGradient id="sunGlow" cx="0.66" cy="0.6" r="0.3">
          <stop offset="0" stop-color="#ffd58a" stop-opacity="0.9"/>
          <stop offset="1" stop-color="#ffd58a" stop-opacity="0"/>
        </radialGradient>
        <linearGradient id="handleSteel" x1="0" y1="0" x2="1" y2="0">
          <stop offset="0" stop-color="#7c8289"/>
          <stop offset="0.5" stop-color="#eef0f2"/>
          <stop offset="1" stop-color="#8a9096"/>
        </linearGradient>
      </defs>
      <rect width="609" height="904" fill="url(#meadowBg)" role="img" aria-label="Soft-focus green meadow with trees and white wildflowers"/>
      <rect width="609" height="904" fill="url(#centerMist)"/>
      <g transform="translate(304 586) rotate(-43)">
        <rect x="-18" y="226" width="36" height="74" fill="url(#handleSteel)"/>
        <rect x="-21" y="292" width="42" height="22" fill="#a4aab0"/>
        <rect x="-28" y="312" width="56" height="200" rx="12" fill="#1e2124"/>
      </g>
      <g role="img" aria-label="Family walking hand in hand through a sunlit meadow, seen from behind">
        <circle cx="304" cy="586" r="218" fill="url(#lensScene)"/>
        <circle cx="304" cy="586" r="218" fill="url(#sunGlow)"/>
      </g>
      <circle cx="304" cy="586" r="218" fill="none" stroke="var(--lens-edge)" stroke-width="4"/>
      <circle cx="304" cy="586" r="226" fill="none" stroke="var(--ring)" stroke-width="13"/>
    </svg>
    <h1 class="title title-top">LANTERNS</h1>
    <p class="title title-mid">OVER THE COPPER</p>
    <p class="title title-main">MEADOW</p>
    <p class="author">R. DALTON MERCER, PhD</p>
  </div>
</body>
</html>
```